Engine Oil shape Bottle Design

I want to design new Plastic bottles 4L and 5L for our brand ( engine oil ) products, design the bottle new and creative shape with its sticker
Our brand name is “Tervik “ as its attached logos

Low design quality

Target Market(s)

Engine oil market

Industry/Entity Type

Cars and trucks engine oil

Font styles to use
Serif
Sans Serif

Requirements
Must have
• Creative design
Nice to have
• New and creative shape
Should not have
• The shape of global brands ، no copy paste from another brands

```html
<!DOCTYPE html>
<html lang="en">
<head>
<meta charset="utf-8">
<title>Tervik Engine Oil 4L Label</title>
<link href="https://fonts.googleapis.com/css2?family=Montserrat:wght@600;700;800&family=Russo+One&family=Share+Tech+Mono&display=swap" rel="stylesheet">
<style>
  :root {
    --backdrop: #9b9b9b;
    --navy: #1f3777;
    --royal: #1c4fa3;
    --deep-blue: #263a73;
    --ink: #222a3a;
    --bullet-ink: #2e3c68;
    --racing-red: #b5222a;
    --dark-red: #7d1b22;
    --gold: #e0a92c;
    --gold-light: #f7e08a;
    --silver: #d6d9de;
    --paper: #ffffff;
    --paper-shade: #e4e5e8;
  }
  html, body {
    margin: 0;
    padding: 0;
    width: 1200px;
    height: 2317px;
    overflow: hidden;
    background: var(--backdrop);
  }
  .label {
    position: absolute;
    left: 75px;
    top: 484px;
    width: 1050px;
    height: 1348px;
  }
  .brand-name { font-family: "Montserrat", sans-serif; font-weight: 800; fill: var(--royal); }
  .brand-tagline { font-family: "Montserrat", sans-serif; font-weight: 700; fill: var(--ink); letter-spacing: 6px; }
  .grade { font-family: "Russo One", sans-serif; }
  .api-spec { font-family: "Russo One", sans-serif; fill: var(--navy); }
  .band-text { font-family: "Share Tech Mono", monospace; fill: var(--paper); }
  .benefit { font-family: "Montserrat", sans-serif; font-weight: 700; fill: var(--bullet-ink); font-size: 17px; }
  .origin-small { font-family: "Montserrat", sans-serif; font-weight: 600; fill: var(--paper); }
  .origin-big { font-family: "Montserrat", sans-serif; font-weight: 800; fill: var(--paper); }
  .volume { font-family: "Russo One", sans-serif; fill: var(--paper); }
</style>
</head>
<body>
<svg class="label" viewBox="0 0 792 1017" xmlns="http://www.w3.org/2000/svg">
  <defs>
    <clipPath id="label-outline">
      <path d="M0,90 Q0,5 75,5 L585,92 Q623,100 623,145 L623,330 C623,420 660,470 720,600 Q792,740 792,790 L792,980 Q792,1017 755,1017 L35,1017 Q0,1017 0,980 Z"/>
    </clipPath>
    <linearGradient id="paper-fill" x1="0" y1="0" x2="0" y2="1">
      <stop offset="0" stop-color="var(--paper)"/>
      <stop offset="0.6" stop-color="var(--paper)"/>
      <stop offset="1" stop-color="var(--paper-shade)"/>
    </linearGradient>
    <linearGradient id="blue-fill" x1="0" y1="0" x2="1" y2="1">
      <stop offset="0" stop-color="var(--royal)"/>
      <stop offset="1" stop-color="var(--deep-blue)"/>
    </linearGradient>
    <linearGradient id="gold-fill" x1="0" y1="1" x2="1" y2="0">
      <stop offset="0" stop-color="var(--gold)"/>
      <stop offset="0.5" stop-color="var(--gold-light)"/>
      <stop offset="1" stop-color="var(--gold)"/>
    </linearGradient>
    <linearGradient id="red-grade" x1="0" y1="0" x2="1" y2="0">
      <stop offset="0" stop-color="var(--dark-red)"/>
      <stop offset="1" stop-color="var(--racing-red)"/>
    </linearGradient>
    <linearGradient id="navy-grade" x1="0" y1="0" x2="0" y2="1">
      <stop offset="0" stop-color="var(--royal)"/>
      <stop offset="1" stop-color="var(--navy)"/>
    </linearGradient>
    <linearGradient id="flag-fill" x1="0" y1="0" x2="1" y2="0">
      <stop offset="0" stop-color="var(--paper)"/>
      <stop offset="1" stop-color="var(--silver)"/>
    </linearGradient>
  </defs>

  <g clip-path="url(#label-outline)">
    <rect class="label-ground" width="792" height="1017" fill="url(#paper-fill)"/>
    <polygon class="corner-blue" points="0,0 470,0 150,380 0,420" fill="url(#blue-fill)"/>
    <path class="oil-splash" role="img" aria-label="Golden engine oil splash"
          d="M0,330 C120,230 250,120 340,55 L500,55 C450,160 330,270 180,340 C110,375 50,410 0,445 Z"
          fill="url(#gold-fill)"/>
    <path class="silver-stripe" d="M195,1017 L560,735 Q640,670 680,520 L700,545 Q660,690 580,750 L225,1017 Z" fill="var(--silver)"/>
    <path class="lower-blue" d="M230,1017 L585,752 Q660,690 700,545 L792,690 L792,1017 Z" fill="url(#blue-fill)"/>
    <polygon class="tagline-band" points="0,745 495,745 475,783 0,783" fill="var(--racing-red)"/>
  </g>

  <circle class="brand-disc" cx="165" cy="175" r="118" fill="var(--paper)"/>
  <text class="brand-name" x="165" y="190" font-size="46" text-anchor="middle">TERVIK</text>

  <circle class="brand-dot" cx="105" cy="415" r="36" fill="var(--royal)"/>
  <text class="brand-name" x="160" y="448" font-size="88" textLength="400" lengthAdjust="spacingAndGlyphs">TERVIK</text>
  <text class="brand-tagline" x="75" y="480" font-size="24" textLength="465">ENGINE OIL LUBRICANTS</text>

  <text class="grade" x="70" y="605" font-size="122" fill="url(#red-grade)" textLength="215" lengthAdjust="spacingAndGlyphs">SN</text>
  <text class="api-spec" x="302" y="603" font-size="32" textLength="205" lengthAdjust="spacingAndGlyphs">API SL / CF</text>
  <text class="grade" x="70" y="720" font-size="130" fill="url(#navy-grade)" textLength="455" lengthAdjust="spacingAndGlyphs">5W30</text>

  <text class="band-text" x="75" y="773" font-size="22" textLength="380" lengthAdjust="spacingAndGlyphs">HIGH POWER TECHNOLOGY ENGINE OIL</text>

  <g class="benefits">
    <circle cx="82" cy="822" r="6" fill="none" stroke="var(--bullet-ink)" stroke-width="2"/>
    <text class="benefit" x="110" y="828">MAINTAINS OPTIMUM</text>
    <text class="benefit" x="110" y="848">VISCOSITY AT DIFFERENT</text>
    <text class="benefit" x="110" y="868">TEMPERATURES</text>
    <circle cx="82" cy="902" r="6" fill="none" stroke="var(--bullet-ink)" stroke-width="2"/>
    <text class="benefit" x="110" y="908">INCREASE ENGINE LIFE</text>
    <circle cx="82" cy="942" r="6" fill="none" stroke="var(--bullet-ink)" stroke-width="2"/>
    <text class="benefit" x="110" y="948">REDUCE WEAR</text>
    <text class="benefit" x="110" y="968">AND TEAR</text>
  </g>

  <circle class="origin-seal" cx="628" cy="590" r="90" fill="var(--paper)" stroke="var(--silver)" stroke-width="6"/>
  <circle class="origin-seal-core" cx="628" cy="590" r="64" fill="var(--paper-shade)"/>

  <text class="origin-small" x="602" y="726" font-size="17">made in</text>
  <text class="origin-big" x="602" y="752" font-size="30">UAE</text>
  <rect class="flag-placeholder" role="img" aria-label="Waving national flag ribbon" x="672" y="712" width="72" height="62" rx="6" fill="url(#flag-fill)"/>

  <rect class="partner-badge" x="558" y="798" width="187" height="70" fill="var(--paper)"/>
  <circle class="cert-emblem" cx="505" cy="920" r="46" fill="var(--gold)"/>

  <text class="volume" x="578" y="980" font-size="104" textLength="170" lengthAdjust="spacingAndGlyphs">4L</text>
</svg>
</body>
</html>
```